Plakat für Feinkosthersteller
Zielgruppe
Wir sind ein Feinkosthersteller mit Fokus auf traditionelle schwäbische Produkte, die modern interpretiert und hochwertig hergestellt werden.
Unsere Produkte werden über 24/7-Verkaufsautomaten in Berlin vertrieben.
Unsere Zielgruppe sind junge Familien, zugezogene Schwaben in Berlin sowie Berlinerinnen und Berliner, die längere Zeit im Schwabenland verbracht haben und eine emotionale Verbindung zu schwäbischen Spezialitäten haben.
Die Marke verbindet Heimatgefühl, Qualität und ehrliche Küche mit einem urbanen, zeitgemäßen Auftritt.
Aufgabenstellung
Die zentrale Botschaft des Automaten ist „Heimat auf Knopfdruck“.
Der Verkaufsautomat soll Heimatgefühl, Vertrautheit und Qualität vermitteln – gleichzeitig aber modern, urban und aufmerksamkeitsstark sein.
Das Design soll so auffällig sein, dass man beim Vorbeigehen stehen bleibt und neugierig wird. Der Automat ist 24/7 zugänglich, entsprechend darf und soll er visuell präsent und markant sein.
Pflichtelemente:
– Unser Logo inklusive Korn & Kruste (wird hochgeladen)
– Der Slogan: „Heimat auf Knopfdruck“
Farbwelt:
– Orientierung an den Farben Baden-Württembergs: Gelb und Schwarz
– Gerne kräftig und kontrastreich, aber hochwertig (nicht billig oder grell)
Stil & Wirkung:
– modern, urban, selbstbewusst
– kein Kitsch, keine Trachten- oder Folkloreoptik
– eher zeitgemäß als rustikal
– emotionale Verbindung zu schwäbischer Heimat, aber klar in Berlin verortet
Format & Anwendung:
– Design für die Außenfläche eines Verkaufsautomaten (24/7 sichtbar)
– Bitte so gestalten, dass das Layout auch aus einigen Metern Entfernung gut wirkt

```html
<!DOCTYPE html>
<html lang="de">
<head>
<meta charset="utf-8">
<title>Korn &amp; Kruste – Automatenbeklebung „Heimat auf Knopfdruck“</title>
<link rel="stylesheet" href="https://fonts.googleapis.com/css2?family=Archivo+Black&family=Open+Sans:wght@600&display=swap">
<style>
  :root {
    --stage: #a2acb1;
    --yellow: #f9c400;
    --black: #000000;
    --window-grey: #b3b3b3;
    --window-glass: #ffffff;
    --window-rim: #f2d6d6;
    --cut-red: #e5232d;
    --marker-pink: #e0458f;
    --fold-grey: #8a8a8a;
    --control-grey: #b3b3b3;
    --brand-font: "Archivo Black", sans-serif;
    --label-font: "Open Sans", sans-serif;
  }
  html, body {
    margin: 0;
    padding: 0;
    width: 1200px;
    height: 860px;
    overflow: hidden;
    background: var(--stage);
  }
  .layout { position: relative; width: 1200px; height: 860px; }
  .panel { position: absolute; box-sizing: border-box; overflow: hidden; }
  .panel--side-left { left: 59px; top: 88px; width: 339px; height: 661px; background: var(--black); }
  .panel--front { left: 398px; top: 92px; width: 325px; height: 644px; background: var(--yellow); }
  .panel--controls { left: 723px; top: 88px; width: 75px; height: 648px; background: var(--black); border-bottom: 1px solid var(--cut-red); }
  .panel--hinge { left: 798px; top: 88px; width: 28px; height: 648px; background: var(--yellow); }
  .panel--side-right { left: 826px; top: 88px; width: 311px; height: 661px; background: var(--yellow); border: 1px solid #e8a23a; }

  .brand-name {
    position: absolute;
    margin: 0;
    font-family: var(--brand-font);
    font-weight: 400;
    line-height: 1;
    text-align: center;
    white-space: nowrap;
    display: flex;
    align-items: center;
    justify-content: center;
  }
  .panel--side-left .brand-name { left: 20px; top: 48px; width: 299px; height: 202px; font-size: 36px; color: var(--yellow); }
  .panel--side-right .brand-name { left: 20px; top: 51px; width: 269px; height: 148px; font-size: 30px; color: var(--black); }
  .panel--front .brand-name { left: 87px; top: 533px; width: 151px; height: 89px; font-size: 17px; color: var(--black); }

  .slogan {
    position: absolute;
    top: 302px;
    margin: 0;
    font-family: var(--brand-font);
    font-weight: 400;
    font-size: 58px;
    line-height: 51px;
    text-transform: uppercase;
    white-space: nowrap;
  }
  .slogan span { display: block; }
  .panel--side-left .slogan { left: 45px; color: var(--yellow); }
  .panel--side-right .slogan { left: 36px; color: var(--black); }

  .illustration { position: absolute; }
  .illustration--left { left: 0; top: 536px; width: 266px; height: 125px; background: linear-gradient(160deg, #1a1a1a, #000 70%); }
  .illustration--right { left: 118px; top: 518px; width: 191px; height: 141px; background: linear-gradient(200deg, #f9c400, #eab800); }

  .guide { position: absolute; top: 0; bottom: 0; width: 0; }
  .guide--cut { left: 20px; border-left: 1px dashed var(--cut-red); }
  .guide--fold { left: 305px; top: 8px; bottom: 8px; border-left: 1px dashed var(--fold-grey); }

  .window { position: absolute; left: 46px; top: 31px; width: 233px; height: 396px; background: var(--window-rim); border: 1px solid var(--cut-red); box-sizing: border-box; }
  .window__frame { position: absolute; left: 6px; top: 6px; right: 6px; bottom: 6px; background: var(--window-grey); border: 1px solid var(--marker-pink); }
  .window__glass { position: absolute; left: 11px; top: 8px; right: 11px; bottom: 10px; background: var(--window-glass); }

  .dispenser { position: absolute; left: 87px; top: 452px; width: 151px; height: 62px; background: var(--black); border-radius: 7px; }

  .lock { position: absolute; width: 10px; height: 10px; border-radius: 50%; background: var(--control-grey); border: 1px solid var(--marker-pink); }
  .lock-label, .control__label { font-family: var(--label-font); font-weight: 600; color: var(--cut-red); text-transform: uppercase; white-space: nowrap; }
  .lock-label { position: absolute; font-size: 3.5px; text-align: center; width: 30px; }
  .panel--front .lock { left: 286px; top: 453px; }
  .panel--front .lock-label { left: 277px; top: 446px; }
  .panel--controls .lock { left: 54px; top: 457px; }
  .panel--controls .lock-label { left: 44px; top: 450px; }

  .control {
    position: absolute;
    left: 15px;
    width: 43px;
    background: var(--control-grey);
    border: 1px solid var(--marker-pink);
    border-radius: 3px;
    box-sizing: border-box;
    display: flex;
    align-items: center;
    justify-content: center;
  }
  .control__label { font-size: 3.5px; }
  .control--display { top: 110px; height: 43px; }
  .control--coin-in { top: 211px; height: 28px; }
  .control--keypad { top: 240px; height: 50px; }
  .control--option-a { top: 291px; height: 50px; }
  .control--option-b { top: 342px; height: 50px; }
  .control--coin-out { left: 22px; width: 31px; top: 483px; height: 38px; }
</style>
</head>
<body>
<main class="layout">

  <section class="panel panel--side-left" aria-label="Linke Seitenwand">
    <p class="brand-name">Korn &amp; Kruste</p>
    <h2 class="slogan"><span>Heimat</span><span>auf</span><span>Knopf</span><span>druck</span></h2>
    <div class="illustration illustration--left" role="img" aria-label="Strichzeichnung zweier Maultaschen in Gelb"></div>
  </section>

  <section class="panel panel--front" aria-label="Front mit Sichtfenster">
    <span class="guide guide--cut"></span>
    <span class="guide guide--fold"></span>
    <div class="window">
      <div class="window__frame"><div class="window__glass"></div></div>
    </div>
    <div class="dispenser"></div>
    <p class="brand-name">Korn &amp; Kruste</p>
    <span class="lock-label">Schloss</span>
    <span class="lock"></span>
  </section>

  <section class="panel panel--controls" aria-label="Bedienleiste">
    <div class="control control--display"><span class="control__label">Display</span></div>
    <div class="control control--coin-in"><span class="control__label">Münzeinwurf</span></div>
    <div class="control control--keypad"><span class="control__label">Tastenfeld</span></div>
    <div class="control control--option-a"><span class="control__label">Optionen</span></div>
    <div class="control control--option-b"><span class="control__label">Optionen</span></div>
    <span class="lock-label">Schloss</span>
    <span class="lock"></span>
    <div class="control control--coin-out"><span class="control__label">Münzauswurf</span></div>
  </section>

  <div class="panel panel--hinge"></div>

  <section class="panel panel--side-right" aria-label="Rechte Seitenwand">
    <p class="brand-name">Korn &amp; Kruste</p>
    <h2 class="slogan"><span>Heimat</span><span>auf</span><span>Knopf</span><span>druck</span></h2>
    <div class="illustration illustration--right" role="img" aria-label="Strichzeichnung zweier Maultaschen in Schwarz"></div>
  </section>

</main>
</body>
</html>
```